Commercial Flooring Contractor Website ($100 Bonus)

We are working with a new commercial flooring contractor in California. They work on schools, hospitals, and government projects.
A few websites for inspiration:
https://trimcoverwork.example (These guys are competitors and provide the same work our client does).
https://zqpavingsco.example (Although NOT a contractor, the simplicity of this site is stunning).
https://www.quietrapid.example (NOT a flooring contractor, but this site is modern, and has a boldness to it).
https://www.dawnfoldatelier.example/en-us (website for an Architectural office that is clean and showcases their work. I can see this working for a flooring contractor).
Thank you for taking the time to consider designing a website for us. We are web developers based in Stockton, CA, USA. Most of our projects go through the same process. Understanding this process may help you win a project with us. We custom-code all of our websites in-house. We don’t have any requirements as to what tools you use for your design, but we ask that you follow these guidelines.
IMAGES:
If you use any images or icons in the design, we ask that you have a link to the asset so we can purchase the image/icon. Most of the designs we submit do not have the customer’s images on them unless they have some great images. Be creative; show us the feeling you are trying to portray with your image choices. Use any royalty-free site you choose. We subscribe to Velto and mainly use their images, but we can purchase images outside of Velto.
FONTS:
We ask that you identify the fonts you’re using in the design. This can be done in a message if you want. We typically use Google Fonts and Velto Fonts.
CONTENT:
We're always open to different content and ideas. We often submit designs with stock images so the client can see our vision. We typically take pictures after the website launch to use their images with our vision. Lorem Ipsum is fine for paragraphs, but we ask that you make the Headers with correct English. We want to be able to show the vision and identify the sections of the website.
INSPIRATION:
We typically add a couple of links in the brief of websites we like to help you get started in your design.
REVISIONS:
We do not often ask for revisions of the designs unless we see something in the design that may not appeal to the client. If there are slight changes that we want to make, we do that in the development process.
FEEDBACK:
We rarely give feedback on designs during the design process. We are working on many website projects and do not have the time to provide feedback. We usually respond if your request is well thought out and asks specific questions, but a note asking “feedback, please” usually goes unanswered.
1 page

```html
<!DOCTYPE html>
<html lang="en">
<head>
<meta charset="utf-8">
<title>Slateway Flooring — Commercial Flooring Contractor</title>
<link href="https://fonts.googleapis.com/css2?family=Fraunces:opsz,wght@9..144,400;9..144,500&family=Jost:wght@400;500;600&display=swap" rel="stylesheet">
<style>
:root{
  --ink:#1d1d1d;
  --text:#3c3c3c;
  --accent:#ef5b5b;
  --pink:#fbe3e3;
  --mint:#e6f1e6;
  --mint-deep:#c8dfc8;
  --rule:#d9c9c9;
  --footer:#545a56;
  --footer-box:#3f423f;
  --bottom:#383a39;
  --white:#fff;
}
*{margin:0;padding:0;box-sizing:border-box}
html,body{width:1200px;height:4989px;overflow:hidden;background:var(--white)}
body{position:relative;font-family:"Jost",sans-serif;color:var(--text)}
.abs{position:absolute}
.photo{position:absolute;z-index:1}
.disc{position:absolute;border-radius:50%}
h1,h2{font-family:"Fraunces",serif;font-weight:400;color:var(--ink);position:absolute;letter-spacing:-.5px;white-space:nowrap;z-index:3}
.copy{position:absolute;font-size:12px;line-height:26px;color:var(--text);z-index:3}
.copy p+p{margin-top:26px}
.btn{position:absolute;z-index:3;height:32px;display:flex;align-items:center;justify-content:space-between;padding:0 20px 0 24px;font-size:10px;letter-spacing:1px;text-transform:uppercase;color:var(--white)}
.btn svg{width:30px;height:8px}
.btn--red{background:var(--accent)}
.btn--dark{background:#4e5150}
.btn--outline{border:1.5px solid #555;color:#333}
.rule{position:absolute;height:1px;background:var(--rule);z-index:3}
/* header */
.brand{left:152px;top:50px;display:flex;align-items:center;gap:12px;font-family:"Jost",sans-serif;font-weight:600;font-size:30px;color:var(--accent)}
.brand i{width:16px;height:16px;border-radius:50%;background:var(--accent);display:block}
.topline{left:348px;width:674px;height:1px;background:#999}
.nav{left:348px;top:62px;width:674px;display:flex;font-size:11px;text-transform:uppercase;color:#333}
.nav a{text-decoration:none;color:inherit;margin-left:104px;letter-spacing:.3px}
.nav a:first-child{margin-left:122px;font-weight:600}
.contact-top{top:18px;display:flex;align-items:center;gap:10px;font-size:10px;color:#333}
.contact-top span.dot{width:18px;height:18px;border-radius:50%;background:var(--accent);display:flex;align-items:center;justify-content:center}
.burger{left:1130px;top:34px;width:32px}
.burger i{display:block;height:1.5px;background:#999;margin-bottom:7px}
/* services list */
.features{left:652px;top:2052px;list-style:none;font-size:12px;color:#333;z-index:3}
.features li{height:30.6px;display:flex;align-items:center;gap:14px}
.features li::before{content:"";width:6px;height:6px;border:1.5px solid var(--accent);border-left:none;border-bottom:none;transform:rotate(45deg)}
/* footer */
.footer{left:0;top:4470px;width:1200px;height:449px;background:var(--footer)}
.footer-bottom{left:0;top:4919px;width:1200px;height:70px;background:var(--bottom);color:#ddd;font-size:10px;display:flex;align-items:center;justify-content:center}
.links{left:519px;top:4578px;color:#eee;font-size:10px;text-transform:uppercase;list-style:none}
.links li{height:36.5px}
.links li:first-child{font-weight:600;height:37px}
.contact-box{left:753px;top:4563px;width:296px;height:228px;background:var(--footer-box);color:#eee}
.cb-row{position:absolute;left:30px;display:flex;gap:22px;align-items:flex-start}
.cb-row small{display:block;font-size:6px;font-weight:600;letter-spacing:.5px;text-transform:uppercase;margin-bottom:4px}
.cb-row div{font-size:12px;line-height:13px}
</style>
</head>
<body>

<!-- header -->
<div class="disc" style="left:1060px;top:-130px;width:260px;height:260px;background:var(--mint)"></div>
<div class="abs brand"><i></i>Slateway</div>
<div class="abs contact-top" style="left:702px"><span class="dot"><svg width="9" height="9" viewBox="0 0 24 24"><path fill="#fff" d="M6.6 10.8a15 15 0 006.6 6.6l2.2-2.2a1 1 0 011-.25 11 11 0 003.6.6 1 1 0 011 1V20a1 1 0 01-1 1A17 17 0 013 4a1 1 0 011-1h3.5a1 1 0 011 1 11 11 0 00.6 3.6 1 1 0 01-.25 1z"/></svg></span>(555) 014-2290</div>
<div class="abs contact-top" style="left:850px"><span class="dot"><svg width="9" height="9" viewBox="0 0 24 24"><path fill="#fff" d="M3 5h18v14H3zM3 6l9 7 9-7" stroke="#ef5b5b" stroke-width="1.5"/></svg></span>hello@slatewayfloors.example</div>
<div class="topline" style="position:absolute;top:46px"></div>
<nav class="abs nav"><a>Home</a><a>About</a><a>Services</a><a>Careers</a></nav>
<div class="topline" style="position:absolute;top:91px"></div>
<div class="abs burger"><i></i><i></i><i></i></div>

<!-- hero -->
<div class="abs" style="left:152px;top:200px;font-size:7px;letter-spacing:2px;transform:rotate(-30deg);transform-origin:left">SCROLL DOWN</div>
<div class="abs" style="left:184px;top:222px;width:1px;height:110px;background:#888"></div>
<div class="abs" style="left:181px;top:226px;width:7px;height:7px;border-radius:50%;background:var(--accent)"></div>
<div class="disc" style="left:54px;top:290px;width:174px;height:174px;background:var(--pink)"></div>
<div class="photo" role="img" aria-label="Bright lobby with floor-to-ceiling windows and polished white floor" style="left:490px;top:174px;width:561px;height:629px;background:linear-gradient(160deg,#f4f6f6,#dde3e2 45%,#f7f8f8)"></div>
<div class="photo" role="img" aria-label="City office towers above a paved plaza" style="left:1070px;top:315px;width:130px;height:488px;background:linear-gradient(180deg,#cfe0ea,#9aa6ad 60%,#b8bcbd)"></div>
<h1 style="left:151px;top:362px;font-size:74px;line-height:93px">Flooring Done<br>Right, Every Time.</h1>
<div class="rule" style="left:151px;top:563px;width:251px;background:#bbb"></div>
<div class="copy" style="left:151px;top:626px;width:290px">Lorem Ipsum is simply dummy text of the printing and typesetting industry. Lorem Ipsum has been the industry's standard dummy text ever since the 1500s</div>
<div class="btn btn--red" style="left:151px;top:768px;width:170px">Contact us<svg viewBox="0 0 30 8"><path d="M0 4h28M24 1l4 3-4 3" stroke="#fff" fill="none"/></svg></div>
<div class="abs" style="left:490px;top:853px;width:710px;height:1px;background:#ccc"></div>
<div class="abs" style="left:490px;top:852px;width:300px;height:2px;background:var(--accent)"></div>

<!-- about -->
<div class="photo" role="img" aria-label="School hallway with blue and yellow lockers and glossy floor" style="left:149px;top:956px;width:441px;height:449px;background:linear-gradient(180deg,#eef0f2,#c9d3de 40%,#e3c86a 55%,#edf0f2)"></div>
<div class="disc" style="left:971px;top:939px;width:166px;height:166px;background:var(--pink)"></div>
<h2 style="right:151px;top:962px;font-size:66px;line-height:82px;text-align:right">About Slateway<br>Flooring</h2>
<div class="rule" style="left:797px;top:1144px;width:252px;background:#e8a3a3"></div>
<div class="photo" role="img" aria-label="Modern lounge with leather sofa on polished white floor" style="left:668px;top:1209px;width:381px;height:449px;background:linear-gradient(180deg,#f2f4f5,#d7dcdc 55%,#c98a3f 70%,#eef0f0)"></div>
<div class="copy" style="left:180px;top:1440px;width:410px"><p>Lorem Ipsum is simply dummy text of the printing and typesetting industry. Lorem Ipsum has been the industry's standard dummy text ever since the 1500s</p><p>It was popularised in the 1960s with the release of Letraset sheets containing Lorem Ipsum passages, and more recently with desktop publishing.</p></div>
<div class="btn btn--dark" style="left:180px;top:1664px;width:170px">Read more<svg viewBox="0 0 30 8"><path d="M0 4h28M24 1l4 3-4 3" stroke="#fff" fill="none"/></svg></div>

<!-- professional services -->
<div class="abs" style="left:0;top:1784px;width:1200px;height:679px;background:var(--mint)"></div>
<div class="disc" style="left:894px;top:1809px;width:174px;height:174px;background:var(--mint-deep)"></div>
<h2 style="left:468px;top:1862px;font-size:45px;line-height:64px;letter-spacing:-1px">Professional Services,<br>Personalized Just For You</h2>
<div class="rule" style="left:468px;top:2006px;width:581px;background:#b9c9b9"></div>
<div class="photo" role="img" aria-label="Clean hospital corridor with hospital bed" style="left:149px;top:1931px;width:460px;height:441px;background:linear-gradient(180deg,#d6e6f0,#9fc0d8 45%,#e9eff3)"></div>
<ul class="abs features">
<li>Bondability Up to 20 Million</li>
<li>Experience Modification Rate .60 – .64</li>
<li>Installers Certified for Secure Entities</li>
<li>Overnight &amp; Weekend Work Capacity</li>
<li>Design/Build Expertise</li>
<li>Value-Engineering Analysis</li>
<li>Specification &amp; Budgeting Assistance</li>
<li>Supplier Negotiations &amp; Scaled Pricing</li>
<li>Material Warehousing for Ongoing Jobs</li>
</ul>

<!-- our services -->
<div class="disc" style="left:54px;top:2541px;width:174px;height:174px;background:var(--pink)"></div>
<h2 style="left:151px;top:2560px;font-size:66px;line-height:82px">Our Services</h2>
<div class="btn btn--red" style="left:896px;top:2591px;width:153px">View all<svg viewBox="0 0 30 8"><path d="M0 4h28M24 1l4 3-4 3" stroke="#fff" fill="none"/></svg></div>
<div class="photo" role="img" aria-label="Concrete arches over a polished concrete floor" style="left:149px;top:2688px;width:441px;height:371px;background:linear-gradient(160deg,#b9bbbc,#e3e4e4 50%,#c6c8c9)"></div>
<div class="abs" style="left:187px;top:2990px;font-family:'Fraunces',serif;font-size:29px;color:#222;z-index:3">Concrete</div>
<div class="abs" style="left:500px;top:2988px;width:52px;height:52px;border-radius:50%;background:var(--accent);display:flex;align-items:center;justify-content:center;z-index:3"><svg width="18" height="18" viewBox="0 0 18 18"><path d="M3 15L15 3M7 3h8v8" stroke="#fff" fill="none" stroke-width="1.4"/></svg></div>
<div class="abs" style="left:333px;top:3030px;font-family:'Fraunces',serif;font-size:66px;color:transparent;-webkit-text-stroke:1px #f1c3c3;z-index:3">01</div>
<div class="photo" role="img" aria-label="Worker finishing wood with a brush" style="left:609px;top:2688px;width:229px;height:333px;background:linear-gradient(160deg,#e6a25a,#c47a3a 50%,#e8d2b0)"></div>
<div class="photo" role="img" aria-label="Asphalt shingle roof with trees behind" style="left:859px;top:2688px;width:228px;height:333px;background:linear-gradient(180deg,#c6d6c4,#5b5e60 35%,#3d3f41)"></div>
<div class="photo" role="img" aria-label="Polished floor in a bright interior" style="left:1107px;top:2688px;width:93px;height:333px;background:linear-gradient(180deg,#dfe9ef,#f1f3f4)"></div>
<div class="abs" style="left:642px;top:3053px;width:558px;height:1px;background:#ddd"></div>
<div class="abs" style="left:642px;top:3052px;width:161px;height:2px;background:var(--accent)"></div>

<!-- careers -->
<div class="photo" role="img" aria-label="Worker operating an orange floor buffing machine" style="left:0;top:3183px;width:1200px;height:575px;background:linear-gradient(90deg,#eef0f1 0%,#e2e5e6 40%,#5a5a5a 60%,#e0682e 80%,#3a3a3a 100%)"></div>
<div class="disc" style="left:45px;top:3222px;width:174px;height:174px;background:#a9acab;z-index:2"></div>
<h2 style="left:149px;top:3276px;font-size:66px;line-height:82px">Careers</h2>
<div class="copy" style="left:149px;top:3386px;width:370px;font-size:12px;line-height:23px"><p>Lorem Ipsum is simply dummy text of the printing and typesetting industry. Lorem Ipsum has been the industry's standard dummy text ever since the 1500s</p><p style="margin-top:20px">It was popularised in the 1960s with the release of Letraset sheets containing Lorem Ipsum passages, and more recently with desktop publishing.</p></div>
<div class="btn btn--outline" style="left:149px;top:3580px;width:171px">Apply now<svg viewBox="0 0 30 8"><path d="M0 4h28M24 1l4 3-4 3" stroke="#333" fill="none"/></svg></div>

<!-- stay in touch -->
<div class="photo" role="img" aria-label="Glass atrium with reflective marble floor" style="left:286px;top:3874px;width:385px;height:449px;background:linear-gradient(90deg,#9ea3a6,#e4e6e7 40%,#c3c7c9)"></div>
<div class="photo" role="img" aria-label="Grey stairwell with window" style="left:75px;top:4152px;width:194px;height:225px;background:linear-gradient(160deg,#8f9192,#d3d4d4 60%,#7a7c7d)"></div>
<div class="disc" style="left:935px;top:3851px;width:174px;height:174px;background:var(--pink)"></div>
<h2 style="right:151px;top:3906px;font-size:66px;line-height:82px">Stay In Touch!</h2>
<div class="copy" style="right:151px;top:4022px;width:340px;text-align:right;font-size:12px;line-height:23px"><p>Lorem Ipsum is simply dummy text of the printing and typesetting industry. Lorem Ipsum has been the industry's standard dummy text ever since the 1500s</p><p style="margin-top:20px">It was popularised in the 1960s with the release of Letraset sheets containing Lorem Ipsum passages, and more recently with desktop publishing.</p></div>
<div class="btn btn--red" style="left:875px;top:4214px;width:174px">Get a quote<svg viewBox="0 0 30 8"><path d="M0 4h28M24 1l4 3-4 3" stroke="#fff" fill="none"/></svg></div>

<!-- footer -->
<div class="abs footer"></div>
<div class="abs brand" style="left:170px;top:4652px;color:#eee"><i style="background:#eee"></i>Slateway</div>
<div class="disc" style="left:183px;top:4783px;width:21px;height:21px;background:var(--accent)"></div>
<div class="disc" style="left:224px;top:4783px;width:21px;height:21px;background:var(--accent)"></div>
<div class="disc" style="left:265px;top:4783px;width:21px;height:21px;background:var(--accent)"></div>
<div class="disc" style="left:305px;top:4783px;width:21px;height:21px;background:var(--accent)"></div>
<ul class="abs links"><li>Quick links</li><li>Home</li><li>About</li><li>Services</li><li>Careers</li><li>Contact us</li></ul>
<div class="abs contact-box">
  <div class="cb-row" style="top:34px"><svg width="16" height="12" viewBox="0 0 16 12"><rect width="16" height="12" fill="#eee"/><path d="M0 0l8 6 8-6" stroke="#3f423f" fill="none"/></svg><div><small>Mail</small>hello@slatewayfloors.example</div></div>
  <div class="cb-row" style="top:96px"><svg width="16" height="16" viewBox="0 0 16 16"><path d="M15 1L1 7l6 2 2 6z" fill="#eee"/></svg><div style="font-size:11px"><small>Address</small>418 N LINDEN AVE, MAPLE CITY,<br>CA 90000 LIC #500111</div></div>
  <div class="cb-row" style="top:160px"><svg width="16" height="16" viewBox="0 0 24 24"><path fill="#eee" d="M6.6 10.8a15 15 0 006.6 6.6l2.2-2.2a1 1 0 011-.25 11 11 0 003.6.6 1 1 0 011 1V20a1 1 0 01-1 1A17 17 0 013 4a1 1 0 011-1h3.5a1 1 0 011 1 11 11 0 00.6 3.6 1 1 0 01-.25 1z"/></svg><div style="font-size:15px"><small>Phone</small>(555) 014-2290</div></div>
</div>
<div class="abs footer-bottom">© Copyright © 2023 Slateway Flooring. All rights reserved.</div>

</body>
</html>
```